Business card for real estate agent / office

We're looking for a new business card. We want something that is pretty clean, modern and sleek. Something that also tells people that we are a new age company...cutting edge. Although real estate has been done a certain way the last 100 years, we have energy and vibrance. Company name is Silver Meadow Properties. info can be found here: http://www.smprealtyhub.example/

needs to include: Name, title, phone number, email. our license number also needs to be displayed somewhere.

Target Market(s)

25-55 homeowners or potential homeowners

Industry/Entity Type

Business

Contact Information for Business Card

we need business card designs for real estate agent / office

Font styles to use
Serif

Requirements
Must have
• needs to include: Name, title, phone number, email. our license number also needs to be displayed somewhere and company name.
Nice to have
• placement area for photo

```html
<!DOCTYPE html>
<html lang="en">
<head>
<meta charset="utf-8">
<title>Silver Meadow Properties – Business Card</title>
<link href="https://fonts.googleapis.com/css2?family=Lato:wght@400;700&display=swap" rel="stylesheet">
<style>
  :root {
    --navy: #0a4169;
    --green: #4a9e3a;
    --ink: #1c1c1c;
    --white: #ffffff;
    --backdrop: #ecebe7;
    --photo-light: #d9d9d9;
    --photo-dark: #6e6e6e;
  }
  html, body {
    margin: 0;
    width: 1200px;
    height: 929px;
    overflow: hidden;
    background: var(--backdrop);
    font-family: "Lato", Arial, sans-serif;
  }
  .card {
    position: absolute;
    width: 520px;
    height: 300px;
    overflow: hidden;
    box-shadow: 0 4px 14px rgba(0,0,0,0.18);
  }
  /* Back side */
  .card-back {
    left: 80px;
    top: 150px;
    background: var(--navy);
    color: var(--white);
    text-align: center;
  }
  .brand {
    position: absolute;
    left: 0; right: 0;
    top: 108px;
    display: flex;
    justify-content: center;
    align-items: center;
    gap: 12px;
  }
  .brand-mark {
    width: 22px; height: 22px;
    background: var(--white);
  }
  .brand-name {
    font-size: 26px;
    font-weight: 700;
    color: var(--white);
    letter-spacing: 0.3px;
  }
  .tagline {
    position: absolute;
    left: 0; right: 0;
    bottom: 46px;
    margin: 0;
    font-size: 13px;
    letter-spacing: 0.4px;
  }
  /* Front side */
  .card-front {
    left: 600px;
    top: 470px;
    background: var(--white);
    color: var(--ink);
  }
  .edge-tab {
    position: absolute;
    left: 0; top: 118px;
    width: 12px; height: 46px;
    background: var(--navy);
    border-radius: 0 8px 8px 0;
  }
  .photo-slot {
    position: absolute;
    left: 330px; top: 18px;
    width: 170px; height: 190px;
    background: linear-gradient(160deg, var(--photo-light), var(--photo-dark));
  }
  .wave {
    position: absolute;
    left: 0; top: 0;
    width: 520px; height: 300px;
  }
  .agent-name {
    position: absolute;
    left: 34px; top: 48px;
    margin: 0;
    font-size: 19px;
    font-weight: 700;
    color: var(--navy);
  }
  .agent-title {
    position: absolute;
    left: 34px; top: 74px;
    margin: 0;
    font-size: 14px;
  }
  .address {
    position: absolute;
    left: 96px; top: 134px;
    margin: 0;
    font-size: 12px;
    line-height: 1.35;
  }
  .contact-list {
    position: absolute;
    left: 96px; top: 172px;
    margin: 0; padding: 0;
    list-style: none;
    font-size: 12.5px;
    line-height: 1.5;
  }
  .contact-list li {
    display: flex;
    align-items: center;
    gap: 8px;
  }
  .contact-list svg { width: 11px; height: 11px; fill: var(--navy); flex: none; }
  .web-name { color: var(--green); }
  .license {
    position: absolute;
    right: 26px; top: 222px;
    margin: 0;
    font-size: 12px;
    color: var(--white);
    letter-spacing: 0.3px;
  }
</style>
</head>
<body>

<section class="card card-back" aria-label="Business card back">
  <div class="brand">
    <span class="brand-mark"></span>
    <span class="brand-name">Silver Meadow Properties</span>
  </div>
  <p class="tagline">We Greatly Appreciate Your Referrals</p>
</section>

<section class="card card-front" aria-label="Business card front">
  <div class="edge-tab"></div>
  <div class="photo-slot" role="img" aria-label="Black and white portrait photo of the agent"></div>
  <svg class="wave" viewBox="0 0 520 300" aria-hidden="true">
    <path d="M0 280 C180 284 300 264 360 228 C420 192 460 156 520 146 L520 300 L0 300 Z" fill="var(--green)"/>
    <path d="M0 286 C180 290 300 270 362 234 C422 198 462 163 520 154 L520 300 L0 300 Z" fill="var(--white)"/>
    <path d="M0 290 C185 292 305 274 366 238 C426 202 466 168 520 160 L520 300 L0 300 Z" fill="var(--navy)"/>
    <path d="M0 300 C150 296 260 288 320 272 C270 292 150 300 0 300 Z" fill="var(--green)"/>
  </svg>

  <h1 class="agent-name">Daniel Okafor</h1>
  <p class="agent-title">Broker, Realtor, MBA</p>

  <p class="address">14-02 Harbour Point<br>Singapore 118420</p>

  <ul class="contact-list">
    <li>
      <svg viewBox="0 0 12 12"><path d="M3 0h6v12H3z M4 1v9h4V1z" fill-rule="evenodd"/></svg>
      310 555 0147
    </li>
    <li>
      <svg viewBox="0 0 12 12"><path d="M0 2h12v8H0z M1 3l5 3.5L11 3z" fill-rule="evenodd"/></svg>
      dan@silvermeadowprop.example
    </li>
    <li>
      <svg viewBox="0 0 12 12"><circle cx="5" cy="5" r="3.5" fill="none" stroke="var(--navy)" stroke-width="1.6"/><path d="M7.5 7.5l3.5 3.5" stroke="var(--navy)" stroke-width="1.8"/></svg>
      <span>www.<span class="web-name">silvermeadowprop</span>.example</span>
    </li>
  </ul>

  <p class="license">CA BRE # 02957316</p>
</section>

</body>
</html>
```